Multilingual Website for a Medico Company

We need a multilingual Website for our Medico company that sells gloves and masks, the website should have 3-5 subpages on 5 different languages.

Industry/Entity Type

Medtech

Number of Pages Required

5+ page

Requirements
Must have
• Unique Design - No template
Should not have
• No Templates

```html
<!DOCTYPE html>
<html lang="en">
<head>
<meta charset="utf-8">
<title>Carevane – Checkout</title>
<link href="https://fonts.googleapis.com/css2?family=Heebo:wght@400;500;700&family=Rubik:wght@500;700&display=swap" rel="stylesheet">
<style>
:root{
  --green:#3d7b1e;--green-dark:#24571a;--lime:#8fc620;--nav:#16240d;
  --footer:#1b1d1b;--text:#2a2a2a;--muted:#555;--line:#c9c9c9;
  --row:#f3f3f3;--head:#e1ebcb;--white:#fff;
}
*{box-sizing:border-box;margin:0;padding:0}
html,body{width:1200px;height:3610px;overflow:hidden}
body{position:relative;font-family:"Heebo",sans-serif;color:var(--text);background:var(--white)}
.abs{position:absolute}
.topbar{left:0;top:0;width:1200px;height:33px;background:var(--green);color:var(--white);font-size:14px;font-weight:500}
.topbar span{position:absolute;top:8px}
.nav{left:0;top:33px;width:1200px;height:95px;background:var(--nav)}
.brand{font-family:"Rubik",sans-serif;font-weight:700;color:var(--lime);font-size:36px}
.nav .brand{position:absolute;left:143px;top:22px}
.menu{position:absolute;top:40px;left:433px;display:flex;gap:26px;color:var(--white);font-size:14px;font-weight:700}
.menu .on{text-decoration:underline;text-underline-offset:4px}
.lang{position:absolute;left:963px;top:32px;width:93px;height:32px;border:1px solid #888;border-radius:16px;color:var(--white);font-size:14px;padding:6px 0 0 36px}
.hero{left:0;top:128px;width:1200px;height:405px;background:linear-gradient(90deg,#d9d9db,#ebebed 50%,#d6d6d8)}
.title{left:0;top:625px;width:1200px;text-align:center;font-family:"Rubik",sans-serif;font-weight:700;font-size:40px;color:#161616}
.mark{left:582px;top:588px;width:36px;height:26px;background:var(--green);border-radius:4px}
.h2{font-family:"Rubik",sans-serif;font-weight:500;font-size:18px;color:#161616;letter-spacing:.5px}
.field{position:absolute;width:430px;height:46px;border:1px solid var(--line);font-size:14px;color:var(--muted);padding:13px 16px}
.order{left:144px;top:1437px;width:912px;height:407px;border:1px solid #ddd;font-size:14px}
.order .r{position:absolute;left:0;width:910px}
.order .c1{position:absolute;left:20px}
.order .c2{position:absolute;left:424px}
.split{position:absolute;left:336px;top:0;width:1px;height:405px;background:#ddd}
.ship{font-style:italic;font-size:12px;line-height:24px}
.ship i{display:inline-block;width:9px;height:9px;border:1px solid #444;border-radius:50%;margin-right:14px;vertical-align:-1px}
.ship i.f{background:#222}
.payhead{left:144px;top:1897px;width:912px;height:56px;background:var(--green);color:var(--white);font-weight:700;font-size:15px;padding:19px 28px}
.paybody{left:144px;top:1953px;width:912px;height:568px;border:1px solid #e2e2e2;border-top:0}
.cards{display:flex;gap:9px}
.card{width:70px;height:44px;display:flex;align-items:center;justify-content:center;font-size:12px;font-weight:700;color:var(--white)}
.inp{position:absolute;left:40px;width:628px;height:47px;border:1px solid var(--line);font-size:14px;color:var(--muted);padding:14px 14px}
.chk{position:absolute;left:42px;font-size:14px;color:#444}
.chk b{display:inline-block;width:12px;height:12px;background:#bbb;margin-right:20px;vertical-align:-1px}
.btn{position:absolute;left:39px;top:467px;width:163px;height:48px;border:2px solid var(--green);color:var(--green);font-weight:700;font-size:14px;text-align:center;padding-top:14px}
.news{left:0;top:2601px;width:1200px;height:416px;background:linear-gradient(90deg,#8dc51f 0%,#90c425 50%,#b7d083 62%,#cfd6c9 75%,#b9bcbc 100%)}
.news h3{position:absolute;left:122px;top:96px;font-family:"Rubik",sans-serif;font-weight:700;font-size:40px;color:var(--white)}
.news p{position:absolute;left:122px;top:146px;color:var(--white);font-size:16px;line-height:24px}
.email{position:absolute;left:122px;top:206px;width:384px;height:48px;background:var(--white);font-size:11px;color:#555;padding:18px 15px}
.sub{position:absolute;left:122px;top:269px;width:384px;height:48px;background:var(--green-dark);color:var(--white);font-weight:700;font-size:14px;text-align:center;padding-top:15px}
.footer{left:0;top:3017px;width:1200px;height:593px;background:var(--footer);color:var(--white)}
.feat{position:absolute;top:42px}
.feat b{display:block;font-size:16px;font-weight:700;margin-bottom:8px}
.feat span{font-size:14px}
.fh{position:absolute;top:193px;font-family:"Rubik",sans-serif;font-weight:500;font-size:18px}
.links{position:absolute;top:233px;font-size:14px;line-height:26.5px}
.soc{position:absolute;top:3281px;width:30px;height:30px;border:1.5px solid var(--white);border-radius:50%}
.fcard{position:absolute;top:3510px;width:50px;height:30px;background:var(--white);color:#1a3d8f;font-size:11px;font-weight:700;text-align:center;padding-top:8px}
</style>
</head>
<body>
<header class="abs topbar">
  <span style="left:143px">Shipping and return policies</span>
  <span style="left:697px">
    <svg width="13" height="13" viewBox="0 0 24 24" style="vertical-align:-2px;margin-right:6px"><path fill="#fff" d="M6.6 10.8a15 15 0 0 0 6.6 6.6l2.2-2.2a1 1 0 0 1 1-.25 11.4 11.4 0 0 0 3.6.57 1 1 0 0 1 1 1V20a1 1 0 0 1-1 1A17 17 0 0 1 3 4a1 1 0 0 1 1-1h3.5a1 1 0 0 1 1 1c0 1.25.2 2.45.57 3.57a1 1 0 0 1-.25 1z"/></svg>+000 1234 5678</span>
  <span style="left:881px">
    <svg width="14" height="11" viewBox="0 0 14 11" style="vertical-align:-1px;margin-right:8px"><rect width="14" height="11" fill="#fff"/><path d="M0 0l7 6 7-6" stroke="#3d7b1e" fill="none"/></svg>hello@carevane.example</span>
</header>
<nav class="abs nav">
  <div class="brand">Carevane</div>
  <div class="menu"><span class="on">HOME</span><span>ABOUT</span><span>GLOVES</span><span>MASKS</span><span>CONTACT</span></div>
  <svg class="abs" style="left:825px;top:35px" width="26" height="26" viewBox="0 0 26 26"><circle cx="11" cy="11" r="8" stroke="#5bb52b" stroke-width="2.5" fill="none"/><path d="M17 17l7 7" stroke="#5bb52b" stroke-width="2.5"/></svg>
  <svg class="abs" style="left:869px;top:35px" width="26" height="26" viewBox="0 0 26 26"><circle cx="13" cy="9" r="6" stroke="#5bb52b" stroke-width="2.3" fill="none"/><path d="M2 25c1-6 6-9 11-9s10 3 11 9z" stroke="#5bb52b" stroke-width="2.3" fill="none"/></svg>
  <svg class="abs" style="left:911px;top:32px" width="34" height="30" viewBox="0 0 34 30"><path d="M2 6h5l4 15h15l3-10H9" stroke="#5bb52b" stroke-width="2.3" fill="none"/><circle cx="13" cy="26" r="2" fill="#5bb52b"/><circle cx="24" cy="26" r="2" fill="#5bb52b"/><circle cx="29" cy="5" r="4.5" fill="#8fc620"/></svg>
  <div class="lang">Eng</div>
  <svg class="abs" style="left:976px;top:41px" width="14" height="14" viewBox="0 0 14 14"><circle cx="7" cy="7" r="6" stroke="#fff" fill="none"/><path d="M1 7h12M7 1c-3 3-3 9 0 12M7 1c3 3 3 9 0 12" stroke="#fff" fill="none"/></svg>
</nav>
<div class="abs hero" role="img" aria-label="Smiling medical worker in a white coat, face mask and blue gloves giving two thumbs up"></div>

<main>
  <div class="abs mark"></div>
  <h1 class="abs title">Checkout</h1>
  <h2 class="abs h2" style="left:151px;top:685px">BILLING DETAILS</h2>
  <section class="billing">
    <div class="field" style="left:153px;top:733px">First name</div>
    <div class="field" style="left:153px;top:795px">Last name</div>
    <div class="field" style="left:153px;top:856px">Company name (optional)</div>
    <div class="field" style="left:153px;top:918px">Country / Region</div>
    <div class="field" style="left:153px;top:979px">Street address</div>
    <div class="field" style="left:153px;top:1041px">Town / City</div>
    <div class="field" style="left:153px;top:1102px">County (optional)</div>
    <div class="field" style="left:153px;top:1164px">Postcode</div>
    <div class="field" style="left:153px;top:1225px">Phone</div>
    <div class="field" style="left:153px;top:1287px">Email address</div>
    <div class="field" style="left:617px;top:733px">First name</div>
    <div class="field" style="left:617px;top:795px">Last name</div>
    <div class="field" style="left:617px;top:856px">Company name (optional)</div>
    <div class="field" style="left:617px;top:918px">Country / Region</div>
    <div class="field" style="left:617px;top:979px">Street address</div>
    <div class="field" style="left:617px;top:1041px">Town / City</div>
    <div class="field" style="left:617px;top:1102px">County (optional)</div>
    <div class="field" style="left:617px;top:1164px">Postcode</div>
    <div class="field" style="left:617px;top:1225px;height:108px">Order notes (optional)</div>
  </section>

  <h2 class="abs h2" style="left:144px;top:1389px">YOUR ORDER</h2>
  <section class="abs order">
    <div class="r" style="top:0;height:46px;background:var(--head)"><span class="c1" style="left:16px;top:14px">Product</span><span class="c2" style="left:421px;top:14px">Subtotal</span></div>
    <div class="r" style="top:46px;height:46px"><span class="c1" style="left:16px;top:14px">Sentinels #11 &nbsp;× 1</span><span class="c2" style="left:421px;top:14px">£159.99</span></div>
    <div class="r" style="top:92px;height:66px;background:var(--row)"><span class="c1" style="top:24px">Night Harbor, The (Comic) #33-2 &nbsp;× 1</span><span class="c2" style="top:24px">£599.99</span></div>
    <div class="r" style="top:158px;height:46px"><span class="c1" style="top:14px">Subtotal</span><span class="c2" style="top:14px">£759.98</span></div>
    <div class="r" style="top:204px;height:201px;background:var(--row)">
      <span class="c1" style="top:44px">Shipping</span>
      <span class="c1" style="top:110px">Total</span>
      <div class="c2 ship" style="left:425px;top:14px">
        <div><i class="f"></i>Swift Post UK: Special Delivery: Guaranteed by 1pm: £8.60</div>
        <div><i></i>Swift Post UK: Special Delivery: Guaranteed by 1pm Saturday: £13.32</div>
        <div><i></i>Swift Post UK: Special Delivery: Guaranteed by 9am: £22.50</div>
        <div><i></i>Swift Post UK: Special Delivery: Guaranteed by 9am Saturday: £25.50</div>
      </div>
      <span class="c2" style="top:134px">£768.58</span>
    </div>
    <div class="split"></div>
  </section>

  <div class="abs payhead">CREDIT CARD (PAYSTREAM)</div>
  <section class="abs paybody">
    <p class="abs" style="left:40px;top:51px;font-size:15px;color:#444">Pay with your credit card via Paystream.</p>
    <div class="abs cards" style="left:40px;top:91px">
      <div class="card" style="background:#1d3a8c">Cardia</div>
      <div class="card" style="background:#2f74c6">Amplo</div>
      <div class="card" style="background:#f1f1f1;color:#333">Duocard</div>
    </div>
    <div class="inp" style="top:158px">Card Number *</div>
    <div class="inp" style="top:230px">Expiry Date</div>
    <div class="inp" style="top:302px">Card Code (CVC)</div>
    <div class="chk" style="top:380px"><b></b>Save payment information to my account for future purchases.</div>
    <div class="chk" style="top:420px"><b style="margin-right:17px"></b>I have read and agree to the website terms and conditions</div>
    <div class="btn">PLACE ORDER</div>
  </section>
</main>

<section class="abs news">
  <div class="abs" style="left:785px;top:0;width:415px;height:416px;background:linear-gradient(90deg,rgba(180,200,150,0),#9ea3a3 40%,#7f8686)" role="img" aria-label="Cleaning worker in mask and gloves wiping a table"></div>
  <h3>Join our Newsletter</h3>
  <p>Subscribe to our mailing list to receive updates<br>and promotional offers.</p>
  <div class="email">Enter your E - mail</div>
  <div class="sub">SUBSCRIBE</div>
</section>

<footer class="abs footer">
  <svg class="abs" style="left:142px;top:43px" width="54" height="44" viewBox="0 0 54 44"><path d="M2 6h30v26H2zM32 14h12l8 10v8H32z" fill="#fff"/><circle cx="12" cy="36" r="6" fill="#fff" stroke="#1b1d1b" stroke-width="3"/><circle cx="42" cy="36" r="6" fill="#fff" stroke="#1b1d1b" stroke-width="3"/></svg>
  <div class="feat" style="left:215px"><b>FREE SHIPPING</b><span>Donec auctor odio eget ante tin</span></div>
  <div class="abs" style="left:437px;top:24px;width:1px;height:99px;background:#333"></div>
  <svg class="abs" style="left:452px;top:46px" width="58" height="40" viewBox="0 0 58 40"><path d="M4 12h44M38 3l10 9-10 9M54 28H10M20 19l-10 9 10 9" stroke="#fff" stroke-width="5" fill="none"/></svg>
  <div class="feat" style="left:525px"><b>REFUNDS &amp; EXCHANGES</b><span>Donec auctor odio eget ante tin</span></div>
  <div class="abs" style="left:758px;top:24px;width:1px;height:99px;background:#333"></div>
  <svg class="abs" style="left:785px;top:46px" width="68" height="40" viewBox="0 0 68 40"><rect x="2" y="2" width="64" height="36" rx="3" fill="#fff"/><rect x="10" y="9" width="48" height="22" rx="11" fill="#1b1d1b"/><circle cx="34" cy="20" r="9" fill="#fff"/></svg>
  <div class="feat" style="left:873px"><b>EASY PAYMENT</b><span>Donec auctor odio eget ante</span></div>
  <div class="abs" style="left:130px;top:123px;width:940px;height:1px;background:#333"></div>

  <div class="fh" style="left:142px">CONACT US</div>
  <svg class="abs" style="left:142px;top:236px" width="16" height="22" viewBox="0 0 16 22"><path d="M8 0a8 8 0 0 1 8 8c0 6-8 14-8 14S0 14 0 8a8 8 0 0 1 8-8z" fill="#fff"/><circle cx="8" cy="8" r="3" fill="#1b1d1b"/></svg>
  <div class="links" style="left:176px;top:230px;line-height:19px">Address:<br>480 enim ipsam voluptatem<br>quia voluptas</div>
  <svg class="abs" style="left:142px;top:3335px;top:318px" width="17" height="17" viewBox="0 0 24 24"><path fill="#fff" d="M6.6 10.8a15 15 0 0 0 6.6 6.6l2.2-2.2a1 1 0 0 1 1-.25 11.4 11.4 0 0 0 3.6.57 1 1 0 0 1 1 1V20a1 1 0 0 1-1 1A17 17 0 0 1 3 4a1 1 0 0 1 1-1h3.5a1 1 0 0 1 1 1c0 1.25.2 2.45.57 3.57a1 1 0 0 1-.25 1z"/></svg>
  <div class="links" style="left:175px;top:313px;font-size:16px">+000 9876 5432</div>
  <svg class="abs" style="left:143px;top:352px" width="18" height="13" viewBox="0 0 18 13"><rect width="18" height="13" fill="#fff"/><path d="M0 0l9 7 9-7" stroke="#1b1d1b" fill="none"/></svg>
  <div class="links" style="left:175px;top:345px;font-size:16px">hello@carevane.example</div>
  <div class="links" style="left:176px;top:379px">8am-5pm Mon-Fri CST</div>

  <div class="fh" style="left:446px">QUICK LINKS</div>
  <div class="links" style="left:446px">Home<br>About Us<br>Products<br>FAQ<br>Shop Now</div>
  <div class="fh" style="left:609px">INFORMATION</div>
  <div class="links" style="left:609px">Gift Packs<br>Contact Us<br>International Shipping Info<br>Privacy &amp; Security<br>Satisfaction Guarantee</div>
  <div class="brand abs" style="left:855px;top:185px;font-size:40px">Carevane</div>
  <div class="abs" style="left:130px;top:3488px;top:471px;width:940px;height:1px;background:#333"></div>
  <div class="abs" style="left:142px;top:515px;font-size:16px">© 2020 Carevane | All Rights Reserved | Disclaimer</div>
</footer>
<div class="soc" style="left:904px" aria-label="Social profile"></div>
<div class="soc" style="left:944px" aria-label="Social profile"></div>
<div class="soc" style="left:984px" aria-label="Social profile"></div>
<div class="soc" style="left:1024px" aria-label="Social profile"></div>
<div class="fcard" style="left:811px">Cardia</div>
<div class="fcard" style="left:876px;color:#333">Findpay</div>
<div class="fcard" style="left:941px;background:#2f74c6;color:#fff">Amplo</div>
<div class="fcard" style="left:1006px">Sendly</div>
</body>
</html>
```